We have a parent company, Summit Harbor Group (SHG), that has other company partners. We are looking for ways to incorporate our SHG logo with our network partners, Beacon Ledger and The Blue Gate. My initial thought is to have SHG as front of card logo, and include The Blue Gate and Beacon Ledger logos on back but I'm open to ideas. Card should include website www.summitharborgrp.example (use for reference). Keywords "Tax Services" "Real Estate" "Insurance" "Investments" "Chief Financial Officer"

Industry/Entity Type

Financial

```html
<!DOCTYPE html>
<html lang="en">
<head>
<meta charset="utf-8">
<title>Summit Harbor Group – Business Card</title>
<link rel="stylesheet" href="https://fonts.googleapis.com/css2?family=Open+Sans:wght@400;600;700&display=swap">
<style>
  :root {
    --stage: #e9e7e3;
    --paper: #ffffff;
    --ink: #2b2b2b;
    --night: #1f1f1f;
    --brand-red: #e8202f;
    --brand-blue: #0d56a6;
  }
  * { box-sizing: border-box; margin: 0; padding: 0; }
  html, body { width: 1200px; height: 900px; overflow: hidden; }
  body {
    background: var(--stage);
    font-family: "Open Sans", Arial, sans-serif;
    position: relative;
  }
  .card {
    position: absolute;
    left: 290px;
    width: 620px;
    height: 354px;
    overflow: hidden;
    box-shadow: 0 4px 14px rgba(0,0,0,0.18);
  }
  /* Back side */
  .card-back { top: 66px; background: var(--night); }
  .back-band { position: absolute; left: 0; width: 100%; background: var(--paper); }
  .back-band.upper { top: 200px; height: 30px; }
  .back-band.lower { top: 250px; height: 70px; }
  .back-logo {
    position: absolute; left: 0; right: 0; top: 120px;
    display: flex; align-items: center; justify-content: center; gap: 12px;
    white-space: nowrap;
  }
  .back-logo .mark-dot { width: 34px; height: 34px; border-radius: 50%; background: var(--paper); }
  .back-logo .brand-name { color: var(--paper); font-weight: 600; font-size: 30px; letter-spacing: 1px; }
  .partners {
    position: absolute; left: 0; right: 0; top: 266px;
    display: flex; justify-content: center; align-items: center; gap: 34px;
    white-space: nowrap;
  }
  .partner { display: flex; align-items: center; gap: 8px; font-weight: 700; font-size: 16px; }
  .partner-gate { color: var(--brand-blue); }
  .partner-gate .badge { width: 28px; height: 28px; background: var(--brand-blue); }
  .partner-ledger { color: var(--brand-red); }
  .partner-ledger .badge { width: 26px; height: 26px; border-radius: 50%; background: var(--brand-red); }

  /* Front side */
  .card-front { top: 480px; background: var(--paper); }
  .front-shapes { position: absolute; inset: 0; }
  .holder { position: absolute; left: 76px; top: 30px; white-space: nowrap; }
  .holder-name { color: var(--brand-red); font-weight: 700; font-size: 24px; line-height: 1.1; }
  .holder-title { color: var(--ink); font-size: 14px; margin-top: 2px; }
  .contacts { position: absolute; left: 30px; top: 160px; list-style: none; }
  .contacts li {
    display: flex; align-items: center; gap: 10px;
    font-size: 14px; color: var(--ink); height: 26px; white-space: nowrap;
  }
  .contacts svg { width: 12px; height: 12px; flex: none; }
  .front-logo {
    position: absolute; left: 300px; top: 178px;
    display: flex; align-items: center; gap: 10px;
    white-space: nowrap;
  }
  .front-logo .mark-dot { width: 34px; height: 34px; border-radius: 50%; background: var(--brand-red); }
  .front-logo .brand-name { color: var(--brand-blue); font-weight: 600; font-size: 24px; letter-spacing: 0.3px; }
</style>
</head>
<body>

<section class="card card-back" aria-label="Card back">
  <div class="back-band upper"></div>
  <div class="back-band lower"></div>
  <div class="back-logo">
    <span class="mark-dot"></span>
    <span class="brand-name">Summit Harbor Group</span>
  </div>
  <div class="partners">
    <div class="partner partner-gate"><span class="badge"></span><span>The Blue Gate</span></div>
    <div class="partner partner-ledger"><span class="badge"></span><span>Beacon Ledger</span></div>
  </div>
</section>

<section class="card card-front" aria-label="Card front">
  <svg class="front-shapes" viewBox="0 0 620 354" aria-hidden="true">
    <polygon points="0,10 40,10 22,60 0,60" fill="var(--brand-blue)"/>
    <polygon points="46,10 66,10 48,60 28,60" fill="var(--brand-red)"/>
    <polygon points="0,270 300,320 295,334 0,284" fill="var(--brand-blue)"/>
    <polygon points="312,318 620,318 620,354 296,354" fill="var(--brand-red)"/>
  </svg>

  <div class="holder">
    <p class="holder-name">Daniel Harlow</p>
    <p class="holder-title">Chief Financial Officer</p>
  </div>

  <ul class="contacts">
    <li>
      <svg viewBox="0 0 16 16"><path d="M4 1l3 3-2 2a9 9 0 005 5l2-2 3 3-2 3C7 15 1 9 1 3z" fill="var(--brand-red)"/></svg>
      (044)-555-0142
    </li>
    <li>
      <svg viewBox="0 0 16 16"><rect x="1" y="3" width="14" height="10" fill="var(--brand-red)"/><path d="M1 3l7 6 7-6" stroke="#fff" stroke-width="1.4" fill="none"/></svg>
      info@summitharborgrp.example
    </li>
    <li>
      <svg viewBox="0 0 16 16"><circle cx="8" cy="8" r="7" fill="var(--brand-red)"/><path d="M1 8h14M8 1c3 3 3 11 0 14M8 1c-3 3-3 11 0 14" stroke="#fff" stroke-width="1" fill="none"/></svg>
      www.summitharborgrp.example
    </li>
  </ul>

  <div class="front-logo">
    <span class="mark-dot"></span>
    <span class="brand-name">Summit Harbor Group</span>
  </div>
</section>

</body>
</html>
```